Business Card Design

Attached is my current Business card I do not like it but I must save the logo portion of it. Don't like the color or the lettering am looking for more architectural look in grays or taupe with the green more of a charturese color and the blue a charcoal color on a textured paper that looks more like something high-end that would appeal to an architect or a designer. We make concrete decorative items such as concrete fireplaces, sinks, tops and more.

Target Market(s)

Architects designers of Commercial and Residential - artistic features

Industry/Entity Type

Architect

Contact Information for Business Card

Maren T. Oakes President and Marketing Director
602-418-5563
email maren@velmorstoneworks.example
Showroom "Tavlin Design Center" 4126 W Harlow Row Scottsdale AZ
Fax: 602-871-2046

Font styles to use
Sans Serif

Requirements
Must have
• Architectural
Natural and earthy colors with a touch of color in the existing attached

```html
<!DOCTYPE html>
<html lang="en">
<head>
<meta charset="utf-8">
<title>Velmor Stoneworks — Business Card</title>
<link href="https://fonts.googleapis.com/css2?family=Titillium+Web:wght@300;400;600&display=swap" rel="stylesheet">
<style>
  :root {
    --backdrop: #e4e2de;
    --card-white: #ecedee;
    --card-grey: #7b7c7e;
    --charcoal: #34475b;
    --slate: #727476;
    --chartreuse: #9bb327;
    --ink: #3a4a5c;
    --soft-text: #dcdde0;
    --brand-grey: #8b8d90;
  }
  * { margin: 0; padding: 0; box-sizing: border-box; }
  html, body {
    width: 1200px; height: 1000px; overflow: hidden;
    background: var(--backdrop);
    font-family: "Titillium Web", sans-serif;
  }
  .sheet {
    width: 1200px; height: 1000px;
    display: flex; flex-direction: column; align-items: center; justify-content: center;
    gap: 40px;
  }
  .card {
    position: relative;
    width: 760px; height: 434px;
    overflow: hidden;
    box-shadow: 0 2px 8px rgba(0,0,0,0.12);
  }

  /* Back side */
  .card--back { background: var(--card-grey); }
  .card--back .brand {
    position: absolute; left: 0; right: 0; top: 50%;
    transform: translateY(-50%);
    display: flex; align-items: center; justify-content: center; gap: 12px;
  }
  .card--back .brand-name { color: var(--soft-text); }
  .card--back .brand-square { background: var(--soft-text); }

  .brand-name {
    font-weight: 400; font-size: 30px; letter-spacing: 1.5px;
    text-transform: uppercase; line-height: 1;
  }
  .brand-square { width: 14px; height: 14px; }

  /* Front side */
  .card--front { background: var(--card-white); }
  .card--front .brand {
    position: absolute; left: 42px; top: 150px;
    display: flex; align-items: center; gap: 10px;
  }
  .card--front .brand-name { color: var(--brand-grey); font-size: 26px; }
  .card--front .brand-square { background: var(--chartreuse); width: 12px; height: 12px; }

  .name-band {
    position: absolute; left: 0; top: 246px; width: 470px; height: 46px;
    background: var(--charcoal);
    display: flex; align-items: center; justify-content: flex-end;
    padding-right: 16px;
  }
  .person-name { color: #fff; font-weight: 300; font-size: 32px; letter-spacing: 0.5px; }

  .title-band {
    position: absolute; left: 0; top: 292px; width: 470px; height: 26px;
    background: var(--slate);
    display: flex; align-items: center; justify-content: flex-end;
    padding-right: 16px;
  }
  .person-title { color: var(--soft-text); font-weight: 300; font-size: 15px; letter-spacing: 0.3px; }

  .contact-band {
    position: absolute; left: 470px; top: 206px; right: 0; height: 86px;
    background: var(--chartreuse);
    padding: 10px 0 0 14px;
    list-style: none;
  }
  .contact-band li {
    display: flex; align-items: center; gap: 8px;
    color: var(--ink); font-size: 14px; line-height: 22px; font-weight: 400;
  }
  .contact-band svg { width: 11px; height: 11px; fill: var(--ink); flex: none; }

  .showroom {
    position: absolute; left: 575px; top: 330px;
    font-size: 12px; line-height: 15px; color: var(--slate); font-weight: 400;
  }
  .showroom-name { color: var(--ink); font-weight: 600; }
  .showroom-name span { color: var(--chartreuse); font-weight: 600; }
</style>
</head>
<body>
<main class="sheet">

  <section class="card card--back" aria-label="Card back">
    <div class="brand">
      <span class="brand-square"></span>
      <span class="brand-name">Velmor Stoneworks</span>
    </div>
  </section>

  <section class="card card--front" aria-label="Card front">
    <div class="brand">
      <span class="brand-square"></span>
      <span class="brand-name">Velmor Stoneworks</span>
    </div>

    <div class="name-band"><span class="person-name">Maren T. Oakes</span></div>
    <div class="title-band"><span class="person-title">President &amp; Marketing Director</span></div>

    <ul class="contact-band">
      <li>
        <svg viewBox="0 0 12 12" aria-hidden="true"><path d="M2.4 0.6 4 2.8 3 4.1c.7 1.6 2 2.9 3.6 3.6L7.9 6.7l2.2 1.6-.6 2.2C5.2 10.3 1.7 6.8 1.5 2.5z"/></svg>
        602-418-5563
      </li>
      <li>
        <svg viewBox="0 0 12 12" aria-hidden="true"><rect x="3" y="1" width="6" height="4"/><rect x="1" y="5" width="10" height="6" rx="1"/></svg>
        602-871-2046
      </li>
      <li>
        <svg viewBox="0 0 12 12" aria-hidden="true"><path d="M1 2.5h10v7H1z M1 2.5 6 6.5 11 2.5" stroke="#9bb327" stroke-width="0.8"/></svg>
        maren@velmorstoneworks.example
      </li>
    </ul>

    <address class="showroom" style="font-style:normal">
      <div class="showroom-name">Velmor Stoneworks <span>Showroom</span></div>
      <div>"Tavlin Design Center" 4126 W Harlow Row</div>
      <div>Scottsdale AZ</div>
    </address>
  </section>

</main>
</body>
</html>
```